Startup company business card (Media & Advertising)

we need a business card design for a company that is a startup in the media and aggregation industry. Card needs to look funky and of a new breed/modern and upmarket.

Target Market(s)

advertisers/ brand agencies & media publishers

Industry/Entity Type

Advertising

Contact Information for Business Card

Please ensure the front face signifies our brand (plumvexo.com) and back has details for the contact. Standard contact such as phone , address, email , website etc.

Font styles to use
Other font styles liked:
• use styleguide and logo font and color

Colors

Designer to choose colors to be used in the design.

Requirements
Must have
• We are disrupting the media and agency industry so subtlety would be good to use imagery to signify this
Nice to have
• Please use logo colors for branding
Should not have
• be as creative and provide few options. Pick a brand color from logo and styleguide

```html
<!DOCTYPE html>
<html lang="en">
<head>
<meta charset="utf-8">
<title>plumvexo business cards</title>
<link href="https://fonts.googleapis.com/css2?family=Roboto+Slab:wght@700&family=PT+Serif:wght@400&display=swap" rel="stylesheet">
<style>
  :root {
    --page-bg: #0b0b0c;
    --card-bg: #2a2a2c;
    --card-edge: #e0283f;
    --brand-red: #e5344b;
    --text-light: #f2f2f2;
    --text-muted: #dcdcdc;
    --emboss: #555557;
  }
  html, body {
    margin: 0;
    padding: 0;
    width: 1200px;
    height: 822px;
    overflow: hidden;
    background: var(--page-bg);
  }
  .canvas {
    position: relative;
    width: 1200px;
    height: 822px;
  }
  .card {
    position: absolute;
    width: 480px;
    height: 274px;
    background: var(--card-bg);
    box-sizing: border-box;
    box-shadow: 0 0 0 2px var(--card-edge), 0 18px 40px rgba(0,0,0,0.6);
    border-radius: 2px;
  }
  .card--back { left: 90px; top: 300px; }
  .card--front { left: 630px; top: 248px; box-shadow: 0 0 0 2px var(--card-edge), 0 4px 0 var(--card-edge), 0 8px 0 #8a1a28, 0 10px 0 var(--card-edge), 0 18px 40px rgba(0,0,0,0.6); }

  .brand {
    display: flex;
    align-items: center;
    gap: 14px;
    font-family: "Roboto Slab", serif;
    font-weight: 700;
    letter-spacing: 0.5px;
  }
  .brand__dot {
    width: 46px;
    height: 46px;
    border-radius: 50%;
    background: var(--brand-red);
  }
  .brand__name { font-size: 40px; color: var(--text-light); }

  .card--back .brand { position: absolute; left: 60px; top: 42px; }

  .contact {
    position: absolute;
    left: 120px;
    top: 112px;
    font-family: "PT Serif", serif;
    color: var(--text-muted);
    font-size: 14px;
    line-height: 19px;
  }
  .contact__name {
    font-size: 21px;
    line-height: 24px;
    color: var(--brand-red);
  }
  .contact__role { margin-bottom: 8px; }

  .card--front .brand {
    position: absolute;
    left: 0; right: 0; top: 0; bottom: 0;
    justify-content: center;
  }
  .card--front .brand__dot { background: var(--emboss); width: 54px; height: 54px; }
  .card--front .brand__name { color: var(--emboss); font-size: 44px; }
</style>
</head>
<body>
  <main class="canvas">
    <section class="card card--back" aria-label="Card back with contact details">
      <div class="brand">
        <span class="brand__dot"></span>
        <span class="brand__name">plumvexo</span>
      </div>
      <div class="contact">
        <div class="contact__name">Daniel Marsh</div>
        <div class="contact__role">Managing Director</div>
        <div>044-987 654 321</div>
        <div>info@plumvexo.com</div>
        <div>www.plumvexo.com</div>
        <div>48 Harbour Lane, Suite 2</div>
        <div>Northfield, 560017.</div>
      </div>
    </section>

    <section class="card card--front" aria-label="Card front with brand">
      <div class="brand">
        <span class="brand__dot"></span>
        <span class="brand__name">plumvexo</span>
      </div>
    </section>
  </main>
</body>
</html>
```